Golden Meadow Kit Social Media Graphics

Focusing on the Golden Meadow Kit product (3 product bundle), create 6-7 individual social media graphics (square size). For the color scheme of the graphics, they should all be complementary with the Golden Meadow Kit bottle colors.

Note: each graphic should have one of the pictures of the bottles (3-product bundle) on it and/or one of the images with a person on it (several pics attached to choose from). I even included some real customer “before and afters” pictures…you can use them if you think the quality is good enough.

Target Market(s)

men and women looking for fast, healthy loss

Industry/Entity Type

health and wellness

Requirements
Must have
• the product is a picture of ALL 3 bottles; no single bottles will be selected

```html
<!DOCTYPE html>
<html lang="en">
<head>
<meta charset="utf-8">
<title>Golden Meadow Kit – Social Media Graphics</title>
<link rel="stylesheet" href="https://fonts.googleapis.com/css2?family=Lexend:wght@400;600;700&display=swap">
<style>
:root{
  --stage:#b3b3b3;
  --blue:#3550a6;
  --plum:#74417f;
  --rose:#b73d57;
  --pink-soft:#fbe6f1;
  --pink-light:#fdf2f8;
  --lilac:#efe2f5;
  --ink:#1d1b3a;
  --white:#ffffff;
  --ring-red:#e8505b;
  --ring-blue:#4a56b0;
}
*{box-sizing:border-box;margin:0;padding:0}
html,body{width:1200px;height:719px;overflow:hidden}
body{background:var(--stage);font-family:"Lexend",sans-serif;position:relative;color:var(--ink)}

.card{position:absolute;width:229px;height:229px;overflow:hidden;
  background:linear-gradient(160deg,var(--pink-light) 0%,var(--white) 45%,var(--pink-soft) 100%)}
.card .sheen{position:absolute;inset:0;
  background:repeating-linear-gradient(120deg,transparent 0 38px,rgba(240,190,215,.18) 38px 40px)}
.header{position:absolute;left:0;top:0;width:229px;height:80px;z-index:3}
.title{position:absolute;left:0;top:9px;width:229px;text-align:center;color:var(--white);z-index:4;
  font-size:13.2px;line-height:16.5px;letter-spacing:-.1px}
.title b{font-weight:700;display:block}
.title span{font-weight:400;display:block}

.photo{position:absolute;z-index:2}
.round{border-radius:50%}
.ring{position:absolute;border-radius:50%;border:.8px solid var(--ring-red);z-index:1}
.ring.blue{border-color:var(--ring-blue)}
.halo{position:absolute;border-radius:50%;background:var(--white);z-index:1}

.bottles{position:absolute;z-index:2;border-radius:6px 6px 3px 3px;
  background:linear-gradient(90deg,#e9eef8 0 30%,#f6f0f6 30% 36%,#ece6f2 36% 66%,#f6f0f6 66% 70%,#f3e4ea 70% 100%)}
.bottles::after{content:"";position:absolute;left:0;right:0;bottom:0;height:38%;
  background:linear-gradient(90deg,#3a52a8 0 30%,transparent 30% 36%,#8a5aa8 36% 66%,transparent 66% 70%,#c83a55 70% 100%);
  opacity:.55;border-radius:0 0 3px 3px}

.checks{position:absolute;z-index:3;list-style:none}
.checks li{display:flex;align-items:center;gap:5px;font-size:4.6px;line-height:5px;height:11px;font-weight:400}
.checks svg{width:5.5px;height:5.5px;flex:none}

.icons{position:absolute;z-index:3;list-style:none}
.icons li{position:absolute;display:flex;align-items:center;gap:5px;font-size:3.7px;line-height:4.4px;font-weight:600;text-transform:uppercase;white-space:nowrap}
.icons svg{width:20px;height:20px;flex:none}
</style>
</head>
<body>

<svg width="0" height="0" style="position:absolute">
  <defs>
    <linearGradient id="band" x1="0" y1="0" x2="1" y2="0">
      <stop offset="0" stop-color="#3550a6"/>
      <stop offset=".5" stop-color="#74417f"/>
      <stop offset="1" stop-color="#b73d57"/>
    </linearGradient>
    <linearGradient id="badge" x1="0" y1="0" x2="1" y2="1">
      <stop offset="0" stop-color="#3550a6"/>
      <stop offset="1" stop-color="#b73d57"/>
    </linearGradient>
    <symbol id="wave" viewBox="0 0 229 80" preserveAspectRatio="none">
      <path d="M0 0H229V64C204 50 176 52 146 64C116 76 88 78 60 68C36 60 18 60 0 66Z" fill="url(#band)"/>
    </symbol>
    <symbol id="tick" viewBox="0 0 10 10">
      <circle cx="5" cy="5" r="5" fill="url(#badge)"/>
      <path d="M2.8 5.2 4.4 6.8 7.3 3.6" fill="none" stroke="#fff" stroke-width="1.3" stroke-linecap="round" stroke-linejoin="round"/>
    </symbol>
    <symbol id="badge-icon" viewBox="0 0 20 20">
      <circle cx="10" cy="10" r="9.4" fill="#fff" stroke="#d8c7e4" stroke-width=".6"/>
      <circle cx="10" cy="10" r="7.6" fill="url(#badge)"/>
      <path d="M6.5 10.2 8.9 12.5 13.6 7.6" fill="none" stroke="#fff" stroke-width="1.4" stroke-linecap="round" stroke-linejoin="round"/>
    </symbol>
  </defs>
</svg>

<!-- Card 1 -->
<section class="card" style="left:104px;top:114px">
  <div class="sheen"></div>
  <svg class="header"><use href="#wave"/></svg>
  <h2 class="title"><b>Burn Belly Fat Fast:</b><span>The 3-Part Solution You Need Now!</span></h2>
  <div class="photo" role="img" aria-label="Smiling woman in sportswear holding a bathroom scale and a lime"
       style="left:12px;top:50px;width:100px;height:179px;border-radius:40px 40px 0 0;background:linear-gradient(180deg,#8a5a44,#c9a48f 45%,#2b2b30 100%);z-index:4"></div>
  <div class="halo" style="left:114px;top:81px;width:106px;height:106px"></div>
  <div class="bottles" role="img" aria-label="Golden Meadow Kit: Sugar Balance, Liver Care and Belly Ease bottles" style="left:114px;top:99px;width:105px;height:64px"></div>
  <ul class="checks" style="left:124px;top:176px">
    <li><svg><use href="#tick"/></svg>Melt stubborn belly fat</li>
    <li><svg><use href="#tick"/></svg>Reduce bloating and inflammation</li>
    <li><svg><use href="#tick"/></svg>Get that waistline snatched</li>
    <li><svg><use href="#tick"/></svg>Boost energy and confidence</li>
  </ul>
</section>

<!-- Card 2 -->
<section class="card" style="left:357px;top:114px">
  <div class="sheen"></div>
  <svg class="header"><use href="#wave"/></svg>
  <h2 class="title"><b>Double Your Weight Loss</b><span>With this Powerful Trio!</span></h2>
  <ul class="icons" style="left:12px;top:0">
    <li style="top:72px"><svg><use href="#badge-icon"/></svg>Melt stubborn belly fat</li>
    <li style="top:94px"><svg><use href="#badge-icon"/></svg>Reduce bloating and<br>inflammation</li>
    <li style="top:117px"><svg><use href="#badge-icon"/></svg>Get that waistline<br>snatched</li>
    <li style="top:140px"><svg><use href="#badge-icon"/></svg>Boost energy and<br>confidence</li>
  </ul>
  <div class="ring" style="left:96px;top:85px;width:126px;height:126px"></div>
  <div class="photo round" role="img" aria-label="Hips and waist in pink seamless leggings, hands resting on the hip"
       style="left:101px;top:90px;width:116px;height:116px;background:radial-gradient(circle at 55% 45%,#f4b5c3,#e58aa2 60%,#fbe3ea 100%);border:2px solid #fff"></div>
  <div class="bottles" role="img" aria-label="Golden Meadow Kit three-bottle bundle" style="left:16px;top:172px;width:74px;height:46px"></div>
</section>

<!-- Card 3 -->
<section class="card" style="left:608px;top:114px">
  <div class="sheen"></div>
  <svg class="header"><use href="#wave"/></svg>
  <h2 class="title"><b>Lose Weight Naturally</b><span>Ditch the Prescription Pills &amp;<br>Needles!</span></h2>
  <ul class="checks" style="left:16px;top:86px">
    <li><svg><use href="#tick"/></svg>Melt stubborn belly fat</li>
    <li><svg><use href="#tick"/></svg>Reduce bloating and inflammation</li>
    <li><svg><use href="#tick"/></svg>Get that waistline snatched</li>
    <li><svg><use href="#tick"/></svg>Boost energy and confidence</li>
  </ul>
  <div class="ring blue" style="left:103px;top:100px;width:126px;height:126px"></div>
  <div class="photo round" role="img" aria-label="Customer before and after photos side by side"
       style="left:109px;top:107px;width:112px;height:112px;background:linear-gradient(90deg,#3a2f2c 0 49%,#f2f0ee 49% 51%,#2c2a2d 51% 100%);border:2px solid #fff"></div>
  <div class="bottles" role="img" aria-label="Golden Meadow Kit three-bottle bundle" style="left:13px;top:156px;width:76px;height:47px"></div>
</section>

<!-- Card 4 -->
<section class="card" style="left:860px;top:114px">
  <div class="sheen"></div>
  <div class="photo" role="img" aria-label="Smiling woman in a white crop top leaning on a marble counter with the bottles"
       style="left:103px;top:40px;width:126px;height:189px;background:linear-gradient(180deg,#5a3a30 0%,#f1eef2 40%,#e6e2e8 70%,#d9d6da 100%);z-index:2"></div>
  <svg class="header"><use href="#wave"/></svg>
  <h2 class="title"><b>Tired of Stubborn Belly Fat?</b><span>Discover the Trio That Works!</span></h2>
  <div class="halo" style="left:22px;top:78px;width:78px;height:78px"></div>
  <div class="bottles" role="img" aria-label="Golden Meadow Kit three-bottle bundle" style="left:15px;top:95px;width:89px;height:54px"></div>
  <ul class="checks" style="left:22px;top:162px">
    <li><svg><use href="#tick"/></svg>Melt stubborn belly fat</li>
    <li><svg><use href="#tick"/></svg>Reduce bloating and inflammation</li>
    <li><svg><use href="#tick"/></svg>Get that waistline snatched</li>
    <li><svg><use href="#tick"/></svg>Boost energy and confidence</li>
  </ul>
</section>

<!-- Card 5 -->
<section class="card" style="left:104px;top:367px">
  <div class="sheen"></div>
  <svg class="header"><use href="#wave"/></svg>
  <h2 class="title"><b>Melt Away Belly Fat Faster with</b><span>This Powerful Trio!</span></h2>
  <div class="ring" style="left:6px;top:90px;width:126px;height:126px"></div>
  <div class="photo round" role="img" aria-label="Hips and waist in pink seamless leggings, hands resting on the hip"
       style="left:11px;top:95px;width:116px;height:116px;background:radial-gradient(circle at 55% 45%,#f4b5c3,#e58aa2 60%,#fbe3ea 100%);border:2px solid #fff"></div>
  <div class="bottles" role="img" aria-label="Golden Meadow Kit three-bottle bundle" style="left:137px;top:74px;width:76px;height:46px"></div>
  <ul class="icons" style="left:143px;top:0">
    <li style="top:133px"><svg><use href="#badge-icon"/></svg>Melt stubborn belly fat</li>
    <li style="top:157px"><svg><use href="#badge-icon"/></svg>Reduce bloating and<br>inflammation</li>
    <li style="top:180px"><svg><use href="#badge-icon"/></svg>Get that waistline<br>snatched</li>
    <li style="top:203px"><svg><use href="#badge-icon"/></svg>Boost energy and<br>confidence</li>
  </ul>
</section>

<!-- Card 6 -->
<section class="card" style="left:357.5px;top:367px">
  <div class="sheen"></div>
  <svg class="header"><use href="#wave"/></svg>
  <h2 class="title"><b>Struggling to Lose Weight?</b><span>Discover Our Ultimate Solution!</span></h2>
  <div class="ring" style="left:2px;top:73px;width:112px;height:112px"></div>
  <div class="round" style="position:absolute;left:8px;top:81px;width:98px;height:98px;background:linear-gradient(135deg,var(--blue),var(--plum) 55%,var(--rose));z-index:1"></div>
  <div class="bottles" role="img" aria-label="Golden Meadow Kit three-bottle bundle" style="left:14px;top:104px;width:86px;height:50px"></div>
  <div class="ring blue" style="left:115px;top:72px;width:114px;height:114px"></div>
  <div class="photo round" role="img" aria-label="Customer before and after photos side by side"
       style="left:119px;top:78px;width:102px;height:102px;background:linear-gradient(90deg,#7a6a5e 0 49%,#f2f0ee 49% 51%,#8b6d5a 51% 100%);border:2px solid #fff"></div>
  <ul class="icons" style="left:0;top:0">
    <li style="left:12px;top:196px"><svg><use href="#badge-icon"/></svg>Melt stubborn<br>belly fat</li>
    <li style="left:76px;top:196px"><svg><use href="#badge-icon"/></svg>Reduce bloating and<br>inflammation</li>
    <li style="left:153px;top:196px"><svg><use href="#badge-icon"/></svg>Get that waistline<br>snatched</li>
  </ul>
</section>

<!-- Card 7 -->
<section class="card" style="left:610.5px;top:367px">
  <div class="sheen"></div>
  <div class="photo" role="img" aria-label="Slim woman in white sportswear measuring her waist with a tape measure"
       style="left:0;top:50px;width:229px;height:179px;background:radial-gradient(ellipse 55% 70% at 58% 45%,#c98e6c 0%,#d9a98a 40%,#f5e9ee 75%,transparent 100%);z-index:1"></div>
  <svg class="header"><use href="#wave"/></svg>
  <h2 class="title"><b>Ready to Burn Fat Faster?</b><span>Discover the Golden Meadow Kit!</span></h2>
  <ul class="icons" style="left:9px;top:0">
    <li style="top:145px"><svg><use href="#badge-icon"/></svg>Melt stubborn belly fat</li>
    <li style="top:164px"><svg><use href="#badge-icon"/></svg>Reduce bloating and<br>inflammation</li>
    <li style="top:184px"><svg><use href="#badge-icon"/></svg>Get that waistline<br>snatched</li>
    <li style="top:204px"><svg><use href="#badge-icon"/></svg>Boost energy and<br>confidence</li>
  </ul>
  <div class="halo" style="left:158px;top:172px;width:80px;height:80px;z-index:2"></div>
  <div class="bottles" role="img" aria-label="Golden Meadow Kit three-bottle bundle" style="left:158px;top:187px;width:70px;height:42px;z-index:3"></div>
</section>

</body>
</html>
```